Icecream Label Design [Corla Bright]

Our company distributes ice cream in Japan. We produce a private brand that has always been know as Corlas.

However the brand design is poor and we have poor/almost zero brand recognition in the market. Currently people buy our product because it is made in NEW ZEALAND (quality) and represents very good value for money.

BUT

Going forward we want to market Corlas as a 'HIGH QUALITY' icecream BRAND in Japan. We need a package label that reflects this.

We are expanding the current product range (flavour and size) of our Corla's icecream.

I think this is a great opportunity to get your design exposed in a large Asian market. We have very good distribution channels and will will sell a lot of this ice cream in Japan in the future and the Corlas brand/logo will become well recognized.

Really looking forward to seeing design proposals! Thank you, any questions please ask - MTW

Reason: Good morning all. Thank you for submissions. We are wishing to see more examples so have decided to extend the deadline. Looking forward to seeing your ideas. Thanks! Declan

Hi All,

I have sent through the current Corla's logo. Please feel free to use this logo in your designs if you think it is appropriate. There is also an image of the current label for your reference - emphasis on fresh milk but the overall design is not good hence my request to you all...

Looking forward to your help and further submissions. 

Thanks!

Declan 

Reason: Just finalizing design. Have extended deadline to accommodate this. Your continued support and cooperation appreciated. Thanks! Declan

Reason: Finalizing decision being made. Thanks! Declan

Reason: Will make decision today. Thanks all! Declan

Target Market(s)

Mother's 30-55 (quality ingredients and value for money)

Industry/Entity Type

It Company

Requirements
Must have
• 1. The brand is Corla Bright

2. You are designing a logo that will be used on our 1 litre tub and 500ML pottle. Design specification files are attached*.
*Please note: on both the 1L and 500ML tub space must be left for regulatory information. Image attached showing current regulatory information and and space on the 1L tub.

3. We want to use this logo/branding as a base for all our 4 flavour varieties noted below so the design must be able to accommodate this somehow.

4. Needs to have a text placeholder for Japanese translation. ie: if on the design you use text that says 'Vanilla Ice Cream' then somewhere there needs to be space for the Japanese equivalent バニラ アイスクリーム
Nice to have
• 1. Corlas uses 100% fresh milk and cream. It would be nice to convey this somehow.

2. Perhaps could include text 'Your Fresh Taste of New Zealand'

3. There are 4* flavour varieties.
Vanilla | Strawberry | Chocolate | Green Tea
* it would be nice to have a good Corlas base design/pattern which can then be modified slightly (image, colour etc maybe) to reflect each unique flavour.

```html
<!DOCTYPE html>
<html lang="en">
<head>
<meta charset="utf-8">
<title>Corla Bright – Vanilla Ice Cream Label</title>
<link rel="stylesheet" href="https://fonts.googleapis.com/css2?family=Pacifico&family=Cormorant+SC:wght@600&family=Cinzel:wght@500&family=Noto+Sans+JP:wght@400&display=swap">
<style>
  :root {
    --white: #ffffff;
    --cocoa-deep: #1c1410;
    --cocoa: #2e1f17;
    --cocoa-mid: #5a4530;
    --tan-bottom: #c9ad6a;
    --gold-light: #f3dc8a;
    --gold: #d6ae4c;
    --gold-dark: #9c7326;
    --ink-brown: #3a2516;
    --cream: #f3ecd2;
    --vanilla-petal: #e8dca0;
  }
  html, body {
    margin: 0;
    padding: 0;
    width: 1200px;
    height: 1000px;
    overflow: hidden;
    background: var(--white);
  }
  .canvas {
    position: relative;
    width: 1200px;
    height: 1000px;
    background: var(--white);
  }
  .label {
    position: absolute;
    left: 100px;
    top: 0;
    width: 1000px;
    height: 1000px;
    overflow: hidden;
    background: linear-gradient(180deg, var(--cocoa-deep) 0%, var(--cocoa) 45%, var(--cocoa-mid) 72%, var(--tan-bottom) 100%);
  }
  .label-art {
    position: absolute;
    inset: 0;
  }
  .brand-plate {
    position: absolute;
    left: 155px;
    top: 50px;
    width: 690px;
    height: 420px;
  }
  .brand-plate svg {
    display: block;
  }
  .brand-text {
    position: absolute;
    left: 0;
    right: 0;
    text-align: center;
    margin: 0;
  }
  .brand-name {
    top: 92px;
    font-family: "Pacifico", cursive;
    font-size: 76px;
    line-height: 92px;
    color: var(--ink-brown);
  }
  .brand-tagline {
    top: 314px;
    font-family: "Cormorant SC", serif;
    font-weight: 600;
    font-size: 21px;
    line-height: 23px;
    color: var(--ink-brown);
  }
  .flavour-visual {
    position: absolute;
  }
  .vanilla-flower {
    left: 80px;
    top: 510px;
    width: 430px;
    height: 330px;
    border-radius: 50% 45% 40% 50%;
    background: radial-gradient(ellipse at 55% 50%, var(--vanilla-petal) 0%, #c9b46a 45%, rgba(60,40,25,0.0) 75%);
  }
  .icecream-scoop {
    left: 460px;
    top: 525px;
    width: 305px;
    height: 270px;
    border-radius: 50%;
    background: radial-gradient(circle at 40% 35%, #fbf7e6 0%, var(--cream) 50%, #d9cfa8 100%);
  }
  .flavour-tag {
    position: absolute;
    left: 358px;
    top: 790px;
    width: 290px;
    height: 58px;
    box-sizing: border-box;
    border: 3px solid var(--gold);
    border-radius: 12px;
    background: linear-gradient(180deg, #3a2418, var(--cocoa-deep));
    font-family: "Cinzel", serif;
    font-weight: 500;
    font-size: 36px;
    line-height: 52px;
    letter-spacing: 3px;
    text-align: center;
    color: var(--gold);
  }
  .flavour-jp {
    position: absolute;
    left: 0;
    right: 0;
    top: 860px;
    text-align: center;
    font-family: "Noto Sans JP", sans-serif;
    font-size: 30px;
    color: var(--ink-brown);
  }
  .open-hint {
    position: absolute;
    left: 22px;
    top: 925px;
    font-family: "Noto Sans JP", sans-serif;
    font-size: 13px;
    line-height: 17px;
    color: var(--ink-brown);
  }
  .open-hint svg {
    display: block;
    margin: 6px 0 0 2px;
  }
  .milk-claim {
    position: absolute;
    left: 0;
    right: 0;
    top: 930px;
    text-align: center;
    font-family: "Pacifico", cursive;
    font-size: 22px;
    color: var(--ink-brown);
  }
</style>
</head>
<body>
<div class="canvas">
  <section class="label">
    <svg class="label-art" width="1000" height="1000" viewBox="0 0 1000 1000">
      <defs>
        <linearGradient id="goldPanel" x1="0" y1="0" x2="1" y2="1">
          <stop offset="0" stop-color="#b98a33"/>
          <stop offset="0.45" stop-color="#e9cd78"/>
          <stop offset="1" stop-color="#b48630"/>
        </linearGradient>
        <linearGradient id="goldBand" x1="0" y1="0" x2="1" y2="0">
          <stop offset="0" stop-color="#a97c2c"/>
          <stop offset="0.5" stop-color="#f1d985"/>
          <stop offset="1" stop-color="#c89a3e"/>
        </linearGradient>
      </defs>
      <path role="img" aria-label="Gold engraved floral pattern" d="M0,0 H1000 V440 C760,330 380,240 0,185 Z" fill="url(#goldPanel)"/>
      <path d="M0,205 C350,255 760,340 1000,455" fill="none" stroke="url(#goldBand)" stroke-width="22"/>
      <path d="M0,245 C340,300 740,390 1000,505" fill="none" stroke="#1a110c" stroke-width="40"/>
      <path d="M0,282 C330,340 700,430 1000,555" fill="none" stroke="url(#goldBand)" stroke-width="10"/>
      <path d="M770,425 C880,500 960,600 1000,700" fill="none" stroke="url(#goldBand)" stroke-width="26"/>
    </svg>

    <div class="brand-plate">
      <svg width="690" height="420" viewBox="0 0 690 420">
        <defs>
          <linearGradient id="plateGold" x1="0" y1="0" x2="1" y2="1">
            <stop offset="0" stop-color="#e2c067"/>
            <stop offset="0.5" stop-color="#f7e6a2"/>
            <stop offset="1" stop-color="#c79a3d"/>
          </linearGradient>
        </defs>
        <path d="M80,40 Q345,-10 610,40 Q640,90 690,110 L690,320 Q640,340 610,390 Q345,440 80,390 Q50,340 0,320 L0,110 Q50,90 80,40 Z" fill="#3a2516"/>
        <path d="M98,62 Q345,18 592,62 Q618,105 662,124 L662,306 Q618,325 592,368 Q345,413 98,368 Q72,325 28,306 L28,124 Q72,105 98,62 Z" fill="url(#plateGold)" stroke="#3a2516" stroke-width="3"/>
        <path d="M110,76 Q345,34 580,76 Q604,114 644,132 L644,298 Q604,316 580,354 Q345,397 110,354 Q86,316 46,298 L46,132 Q86,114 110,76 Z" fill="none" stroke="#8a6424" stroke-width="1.5"/>
      </svg>
      <p class="brand-text brand-name">Corla<br>Bright</p>
      <p class="brand-text brand-tagline">Your Fresh Taste<br>of New Zealand</p>
    </div>

    <div class="flavour-visual vanilla-flower" role="img" aria-label="Vanilla flower with leaf and vanilla pods"></div>
    <div class="flavour-visual icecream-scoop" role="img" aria-label="Scoop of vanilla ice cream"></div>

    <div class="flavour-tag">VANILLA</div>
    <div class="flavour-jp">ストローベリーアイスクリーム</div>

    <div class="open-hint">
      開封口 タブを引いて、<br>蓋を開けてください。
      <svg width="22" height="12" viewBox="0 0 22 12"><path d="M0,0 H22 L11,12 Z" fill="#1c1410"/></svg>
    </div>

    <div class="milk-claim">100% fresh milk and cream</div>
  </section>
</div>
</body>
</html>
```